DELVANE ROOFING YARD SIGN

We need a yard sign to put in our customers' yards when we are roofing their home.
Delvane Roofing
468 Pettigrew Rd
Lake Charles LA 70452
phone: 337-555-0148

Maybe some verbiage like "Your Hometown Roofing Experts"
or
"Family Owned Since 1956"

```html
<!DOCTYPE html>
<html lang="en">
<head>
<meta charset="utf-8">
<title>Delvane Roofing Yard Sign</title>
<link rel="stylesheet" href="https://fonts.googleapis.com/css2?family=Playfair+Display:wght@400;500&family=Poppins:wght@400;500&display=swap">
<style>
  :root {
    --page-bg: #efede8;
    --sign-white: #ffffff;
    --gold-deep: #a8672b;
    --gold-mid: #cf9346;
    --gold-light: #e2bd63;
    --brown-text: #8a5a2b;
    --ink: #141414;
    --band-black: #000000;
  }
  html, body {
    margin: 0;
    padding: 0;
    width: 1200px;
    height: 848px;
    overflow: hidden;
    background: var(--page-bg);
  }
  .canvas {
    position: relative;
    width: 1200px;
    height: 848px;
  }
  .yard-sign {
    position: absolute;
    left: 104px;
    top: 35px;
    width: 991px;
    height: 778px;
    display: block;
  }
  .sign-board { fill: var(--sign-white); }
  .band-black { fill: var(--band-black); }
  .band-rule { fill: none; stroke: var(--gold-mid); stroke-width: 3; }
  .side-note {
    font-family: "Playfair Display", serif;
    font-size: 29px;
    fill: var(--brown-text);
  }
  .tagline {
    font-family: "Playfair Display", serif;
    font-size: 62px;
    fill: var(--ink);
  }
  .phone {
    font-family: "Poppins", sans-serif;
    font-size: 84px;
    font-weight: 400;
    letter-spacing: 2px;
  }
  .address {
    font-family: "Poppins", sans-serif;
    font-size: 16px;
    font-weight: 500;
    letter-spacing: 6px;
    fill: var(--gold-mid);
  }
  .badge-circle { fill: var(--sign-white); stroke: url(#goldGradient); stroke-width: 20; }
  .badge-name {
    font-family: "Playfair Display", serif;
    font-size: 46px;
    font-weight: 500;
    fill: var(--ink);
  }
</style>
</head>
<body>
<main class="canvas">
  <svg class="yard-sign" viewBox="0 -216 991 778" xmlns="http://www.w3.org/2000/svg" aria-label="Delvane Roofing yard sign">
    <defs>
      <linearGradient id="goldGradient" x1="0" y1="0" x2="1" y2="0">
        <stop offset="0" stop-color="var(--gold-deep)"/>
        <stop offset="0.5" stop-color="var(--gold-light)"/>
        <stop offset="1" stop-color="var(--gold-deep)"/>
      </linearGradient>
    </defs>

    <rect class="sign-board" x="0" y="0" width="991" height="562"/>

    <path class="band-gold" fill="url(#goldGradient)"
          d="M0 224 Q495 310 991 224 L991 426 Q495 320 0 426 Z"/>

    <path class="band-rule" d="M0 480 Q495 360 991 480"/>
    <path class="band-black" d="M0 492 Q495 376 991 492 L991 562 L0 562 Z"/>

    <text class="side-note" x="56" y="83">Family Owned</text>
    <text class="side-note" x="773" y="83">Since 1956</text>

    <text class="tagline" x="495.5" y="352" text-anchor="middle">Your Hometown Roofing Experts</text>

    <text class="phone" x="495.5" y="522" text-anchor="middle" fill="url(#goldGradient)">337-555-0148</text>
    <text class="address" x="495.5" y="550" text-anchor="middle">468 PETTIGREW RD LAKE CHARLES LA 70452</text>

    <g class="brand-badge">
      <circle class="badge-circle" cx="495.5" cy="12" r="219"/>
      <text class="badge-name" x="495.5" y="0" text-anchor="middle">Delvane</text>
      <text class="badge-name" x="495.5" y="56" text-anchor="middle">Roofing</text>
    </g>
  </svg>
</main>
</body>
</html>
```